Velqor5 Business Card - Health

Velqor5 maximizes value from the health data of its clients, including doctors, HMOs, and patients. I have attached the Velqor5 logo as an ai and eps file.
Target Market(s)
Health, HMO, Healthcare, Data, Big Data, Data Analytics
Industry/Entity Type
Business
Requirements
Must have
- At least one side should have some white on it so that we can write on it.

```html
<!DOCTYPE html>
<html lang="en">
<head>
<meta charset="utf-8">
<title>Velqor5 Business Card</title>
<link rel="stylesheet" href="https://fonts.googleapis.com/css2?family=Source+Sans+3:wght@300;400;600&display=swap">
<style>
  :root {
    --stage: #000000;
    --card: #2e2f32;
    --accent: #1b8fe6;
    --text-light: #f2f2f2;
    --brand-grey: #dcdcde;
    --divider: #1f4a55;
    --write-area: #ffffff;
  }
  * { margin: 0; padding: 0; box-sizing: border-box; }
  html, body {
    width: 1200px;
    height: 900px;
    overflow: hidden;
    background: var(--stage);
  }
  body {
    position: relative;
    font-family: "Source Sans 3", "Segoe UI", Arial, sans-serif;
  }
  .card {
    position: absolute;
    top: 271px;
    width: 457px;
    height: 281px;
    background: var(--card);
    border-radius: 14px;
    overflow: hidden;
  }
  .card--front { left: 137px; }
  .card--back { left: 626px; }

  .front-brand {
    position: absolute;
    left: 70px;
    top: 124px;
    width: 120px;
    text-align: center;
    color: var(--accent);
    font-size: 27px;
    font-weight: 600;
    line-height: 1;
  }
  .front-divider {
    position: absolute;
    left: 219px;
    top: 68px;
    width: 1px;
    height: 150px;
    background: var(--divider);
  }
  .contact {
    position: absolute;
    left: 249px;
    top: 64px;
    color: var(--text-light);
    font-size: 13px;
    line-height: 16px;
  }
  .contact__name {
    color: var(--accent);
    font-size: 19px;
    line-height: 22px;
  }
  .contact__title { margin-bottom: 10px; }
  .contact__address { margin-bottom: 10px; }
  .contact__line {
    display: flex;
    align-items: center;
    gap: 7px;
    height: 16.5px;
  }
  .contact__line svg { width: 10px; height: 10px; flex: none; }

  .back-brand {
    position: absolute;
    left: 89px;
    top: 100px;
    display: flex;
    align-items: center;
    gap: 18px;
  }
  .back-brand__dot {
    width: 70px;
    height: 70px;
    border-radius: 50%;
    background: var(--accent);
  }
  .back-brand__name {
    color: var(--brand-grey);
    font-size: 62px;
    font-weight: 300;
    line-height: 1;
  }
  .write-area {
    position: absolute;
    left: 0;
    right: 0;
    bottom: 0;
    height: 52px;
    background: var(--write-area);
  }
</style>
</head>
<body>
  <section class="card card--front">
    <div class="front-brand">Velqor5</div>
    <div class="front-divider"></div>
    <div class="contact">
      <div class="contact__name">Marcus Ellery</div>
      <div class="contact__title">Managing Director</div>
      <div class="contact__address">12345, Address Goes Here<br>Country Name, 123456.</div>
      <div class="contact__line">
        <svg viewBox="0 0 10 10" aria-hidden="true"><path d="M2 0.6 L3.6 2.6 L2.8 3.6 Q3.9 5.9 6.4 7.2 L7.4 6.4 L9.4 8 L8.2 9.4 Q4.2 9 0.6 1.8 Z" fill="var(--accent)"/></svg>
        <span>044-987 210 654</span>
      </div>
      <div class="contact__line">
        <svg viewBox="0 0 10 10" aria-hidden="true"><rect x="0.5" y="2" width="9" height="6.4" fill="var(--accent)"/><path d="M0.5 2 L5 5.6 L9.5 2" stroke="var(--card)" stroke-width="0.9" fill="none"/></svg>
        <span>info@webname.com</span>
      </div>
      <div class="contact__line">
        <svg viewBox="0 0 10 10" aria-hidden="true"><g fill="none" stroke="var(--accent)" stroke-width="1.3" stroke-linecap="round"><path d="M4.2 5.8 L2.6 7.4 A1.4 1.4 0 0 1 0.9 5.6 L2.6 3.9"/><path d="M5.8 4.2 L7.4 2.6 A1.4 1.4 0 0 0 5.6 0.9 L3.9 2.6"/><path d="M3.6 6.4 L6.4 3.6"/></g></svg>
        <span>www.websitename.com</span>
      </div>
    </div>
  </section>

  <section class="card card--back">
    <div class="back-brand">
      <div class="back-brand__dot"></div>
      <div class="back-brand__name">Velqor5</div>
    </div>
    <div class="write-area" role="img" aria-label="Blank white area for handwritten notes"></div>
  </section>
</body>
</html>
```